lotus spoon vietnamese restaurant in need of a new menu

a family owned vietnamese restaurant in need of a new menu design that is fun, classy, and yet simple. menu that will catch the customers eyes. easy to read yet flows nicely. like to use the color green (basil green color) creme yellow and maroon. open to other colors as long as it looks nice together. our restaurant is family oriented, casual yet has a nice ambiance atmosphere.
prefer 11x17 portrait double sided. attached is our menu with the current price updated so use the info on this to start creating! looking for something unique, professional and one of a kind menu!
Updates
please use your own creative layout and design. we are open to ideas. the files uploaded are the updated prices and the logo is to use whichever one you feel goes with the menu.
Reason: don't see anything we like so far...please be creative!
Target Market(s)
restaurant consumers
Industry/Entity Type
Restaurant
Look and feel
Each slider illustrates characteristics of the customer's brand and the style your logo design should communicate.

```html
<!DOCTYPE html>
<html lang="en">
<head>
<meta charset="utf-8">
<title>Lotus Spoon – Take Out Menu</title>
<link href="https://fonts.googleapis.com/css2?family=Arimo:ital,wght@0,400;0,700;1,400&family=Patua+One&display=swap" rel="stylesheet">
<style>
  :root{
    --brown-dark:#2e1d12;
    --brown:#3d2716;
    --brown-mid:#5a3a20;
    --cream:#fdf8d2;
    --cream-deep:#f6ec9a;
    --basil:#7cc242;
    --basil-dark:#4f9a2a;
    --gold:#f2d66c;
    --text-dark:#231a12;
    --text-light:#f4ecc9;
  }
  *{margin:0;padding:0;box-sizing:border-box}
  html,body{width:1200px;height:783px;overflow:hidden;background:#fff}
  .menu{position:relative;width:1200px;height:783px;font-family:"Arimo",Arial,sans-serif}
  .panel{position:absolute;top:0;height:783px;overflow:hidden}
  .panel svg.bg{position:absolute;left:0;top:0}

  /* left panel */
  .panel--veg{left:0;width:393px;background:var(--brown)}
  .section-title{position:absolute;font-family:"Patua One",Georgia,serif;font-size:15px;letter-spacing:.5px;text-align:center}
  .panel--veg .section-title{left:0;width:393px;top:28px;color:var(--gold)}
  .veg-list{position:absolute;left:0;top:68px;width:393px;list-style:none;text-align:center;color:var(--gold)}
  .veg-list li{height:28.5px}
  .item-name{font-size:9.5px;font-weight:700;display:block;line-height:12px}
  .item-desc{font-size:7px;font-style:italic;display:block;line-height:10px}
  .chili{display:inline-block;width:6px;height:8px;background:#f47a20;border-radius:50% 50% 40% 40%;vertical-align:-1px;margin-left:2px}
  .photo-grid{position:absolute;left:74px;top:308px;display:grid;grid-template-columns:118px 118px;column-gap:9px;row-gap:9px}
  .thumb{position:relative;height:73px;border:2px solid var(--basil);border-radius:5px;overflow:hidden}
  .thumb span{position:absolute;right:6px;bottom:4px;font-size:7px;font-weight:700;color:#fff;text-shadow:0 0 2px #000}
  .t1{background:linear-gradient(135deg,#d6c7a6,#b8a079)}
  .t2{background:linear-gradient(135deg,#e8e3d8,#a66b3d)}
  .t3{background:linear-gradient(135deg,#c7451c,#6f2c14)}
  .t4{background:linear-gradient(135deg,#5a3a1c,#3a6b22)}
  .t5{background:linear-gradient(135deg,#9fb57a,#d98a6a)}
  .t6{background:linear-gradient(135deg,#a5642e,#d6b07a)}
  .t7{background:linear-gradient(135deg,#d5d8d2,#b98f7a)}
  .t8{background:linear-gradient(135deg,#e0d4b8,#8a5a2e)}
  .contact{position:absolute;text-align:center;font-size:11px;line-height:15px}
  .contact b{font-weight:700}
  .panel--veg .contact{left:0;width:393px;top:693px;color:var(--brown-dark)}

  /* middle panel */
  .panel--drinks{left:393px;width:392px;background:linear-gradient(180deg,#fffdf0 0%,var(--cream) 55%,var(--cream-deep) 100%)}
  .panel--drinks .section-title{left:0;width:392px;top:28px;color:var(--gold)}
  .drink-list{position:absolute;left:26px;top:66px;width:350px;list-style:none;color:var(--text-dark)}
  .drink-list li{height:29.4px}
  .drink-list .item-name{font-size:8.5px}
  .drink-list .item-desc{font-size:7px;font-style:italic;line-height:9.5px}
  .smoothie{position:absolute;left:26px;top:484px;width:350px;color:var(--text-dark)}
  .smoothie h3{font-size:10px;font-weight:700;margin-bottom:9px}
  .flavours{display:grid;grid-template-columns:137px 137px 90px;font-size:8px;font-weight:700;line-height:11px}
  .extra{margin-top:8px;font-size:7.5px;font-style:italic;font-weight:700}
  .drink-photos{position:absolute;top:567px;left:34px;width:326px;display:flex;justify-content:space-between}
  .drink-photo{width:68px;height:68px;border:1px solid var(--brown);border-radius:5px}
  .dp1{background:linear-gradient(160deg,#6a4a34,#2a1c12)}
  .dp2{background:linear-gradient(160deg,#8fb96a,#5b2f1c)}
  .dp3{background:linear-gradient(160deg,#cdb8d6,#8a6a9a)}
  .fine-print{position:absolute;left:20px;width:352px;top:697px;text-align:center;font-size:7px;font-style:italic;line-height:10px;color:var(--gold)}

  /* right panel */
  .panel--cover{left:785px;width:415px;background:linear-gradient(160deg,#fffde8 0%,var(--cream) 45%,var(--cream-deep) 100%)}
  .brand{position:absolute;left:40px;top:108px;width:340px;text-align:center;color:var(--text-dark)}
  .brand-name{font-size:38px;font-weight:700;line-height:44px;display:flex;align-items:center;justify-content:center;gap:12px}
  .brand-mark{width:14px;height:14px;background:var(--basil);border-radius:50%}
  .brand-tag{font-size:23px;line-height:30px}
  .take-out{position:absolute;left:0;width:415px;top:625px;text-align:center;font-family:"Patua One",Georgia,serif;font-size:20px;color:var(--brown)}
  .panel--cover .contact{left:0;width:415px;top:693px;color:var(--gold)}
</style>
</head>
<body>
<main class="menu">

  <!-- Vegetarian panel -->
  <section class="panel panel--veg">
    <svg class="bg" width="393" height="783" viewBox="0 0 393 783" aria-hidden="true">
      <defs>
        <linearGradient id="vegHeader" x1="0" x2="1">
          <stop offset="0" stop-color="#5a3a20"/><stop offset=".5" stop-color="#6b4a28"/><stop offset="1" stop-color="#3d2716"/>
        </linearGradient>
        <linearGradient id="vegWave" x1="0" y1="0" x2="0" y2="1">
          <stop offset="0" stop-color="#a4d65e"/><stop offset="1" stop-color="#7cc242"/>
        </linearGradient>
      </defs>
      <rect x="0" y="26" width="393" height="24" fill="url(#vegHeader)"/>
      <path d="M0 662 C90 640 150 665 230 668 C300 670 350 652 393 650 L393 783 L0 783 Z" fill="#5a3a20"/>
      <path d="M0 676 C90 652 160 676 240 678 C310 680 355 662 393 660 L393 783 L0 783 Z" fill="url(#vegWave)"/>
    </svg>
    <h2 class="section-title">MON CHAY - VEGETARIAN PLATE</h2>
    <ul class="veg-list">
      <li><span class="item-name">64. GOI CUON TOFU | 4.50</span><span class="item-desc">FRIED TOFU SPRING ROLL</span></li>
      <li><span class="item-name">65. SOUP RAU CAI (S) | 3.00 &nbsp;(L) | 5.95</span><span class="item-desc">VEGETABLES SOUP</span></li>
      <li><span class="item-name">66. PHO DAU HU RAU CAI | 9.50</span><span class="item-desc">FRIED TOFU &amp; VEGETABLES NOODLE SOUP</span></li>
      <li><span class="item-name">67. DAU HU XAO RAU CAI | 9.95</span><span class="item-desc">STIR FRY TOFU WITH MIXED VEGETABLES</span></li>
      <li><span class="item-name">68. DAU HU XAO XA OT | 9.95 <i class="chili"></i></span><span class="item-desc">STIR FRY FRIED TOFU WITH HOT CHILLI &amp; LEMONGRASS</span></li>
      <li><span class="item-name">69. BUN XAO DAU HU RAU CAI | 9.50</span><span class="item-desc">STIR FRY VERMICELLI WITH FRIED TOFU &amp; MIXED VEGETABLES</span></li>
      <li><span class="item-name">70. COM CHIEN DAU HU RAU CAI | 9.50</span><span class="item-desc">FRIED TOFU &amp; VEGETABLES FRIED RICE</span></li>
      <li><span class="item-name">71. BUN DAU HU | 9.25</span><span class="item-desc">FRIED TOFU VERMICELLI BOWL</span></li>
    </ul>
    <div class="photo-grid">
      <div class="thumb t1" role="img" aria-label="Photo of noodle soup dish #10"><span>#10</span></div>
      <div class="thumb t2" role="img" aria-label="Photo of rice plate with egg dish #45"><span>#45</span></div>
      <div class="thumb t3" role="img" aria-label="Photo of glazed chicken wings dish #41"><span>#41</span></div>
      <div class="thumb t4" role="img" aria-label="Photo of stir fried beef with herbs dish #40"><span>#40</span></div>
      <div class="thumb t5" role="img" aria-label="Photo of shrimp salad dish #37"><span>#37</span></div>
      <div class="thumb t6" role="img" aria-label="Photo of fried rice with grilled pork dish #53"><span>#53</span></div>
      <div class="thumb t7" role="img" aria-label="Photo of seafood noodle bowl dish #12"><span>#12</span></div>
      <div class="thumb t8" role="img" aria-label="Photo of grilled pork over rice dish #44"><span>#44</span></div>
    </div>
    <address class="contact">(555) 210-4837<br>2187 <b>W. Harbor Ave</b><br><b>Maple Grove, FL 33090</b></address>
  </section>

  <!-- Beverages panel -->
  <section class="panel panel--drinks">
    <svg class="bg" width="392" height="783" viewBox="0 0 392 783" aria-hidden="true">
      <defs>
        <linearGradient id="bevHeader" x1="0" x2="1">
          <stop offset="0" stop-color="#f6ec9a" stop-opacity="0"/><stop offset=".2" stop-color="#5a3a20"/><stop offset=".8" stop-color="#4a2f1a"/><stop offset="1" stop-color="#f6ec9a" stop-opacity="0"/>
        </linearGradient>
      </defs>
      <rect x="0" y="26" width="392" height="24" fill="url(#bevHeader)"/>
      <path d="M0 668 C100 690 170 672 250 664 C310 658 360 668 392 680 L392 783 L0 783 Z" fill="#3d2716"/>
      <path d="M0 660 C100 684 170 666 250 658 C310 652 360 662 392 672" fill="none" stroke="#c9a04a" stroke-width="1.5"/>
    </svg>
    <h2 class="section-title">BEVERAGES</h2>
    <ul class="drink-list">
      <li><span class="item-name">72. NUOC NGOT - SODA | 1.50</span><span class="item-desc" style="font-style:normal">COLA ▪ DIET COLA ▪ COLA ZERO ▪ CLASSIC COLA ▪ CITRUS DEW ▪ ORANGE SODA<br>CHERRY SPICE ▪ LEMON LIME ▪ CLUB SODA ▪ GINGERALE ▪ ROOT BEER ▪ BOTTLE WATER</span></li>
      <li><span class="item-name">73. NUOC DUA | 4.25</span><span class="item-desc">FRESH COCONUT JUICE</span></li>
      <li><span class="item-name">74. CAM VAT | 4.00</span><span class="item-desc">FRESH ORANGE JUICE</span></li>
      <li><span class="item-name">75. DA CHANH | 3.50</span><span class="item-desc">FRESH LIMEADE JUICE</span></li>
      <li><span class="item-name">76. SODA DA CHANH | 4.00</span><span class="item-desc">FRESH LIMEADE WITH CLUB SODA</span></li>
      <li><span class="item-name">77. THAI ICE TEA | 4.00</span><span class="item-desc">THAI TEA MIX WITH HALF &amp; HALF MILK</span></li>
      <li><span class="item-name">78. SPARKLING MINERAL WATER | 1.95</span></li>
      <li><span class="item-name">79. CAFE SUA DA OR DEN DA | 3.50</span><span class="item-desc">VIETNAMESE MILK ICE COFFEE OR BLACK COFFEE (HOT OR COLD)</span></li>
      <li><span class="item-name">80. CHANH MUOI | 3.50</span><span class="item-desc">SALTY BRINED LIME JUICE</span></li>
      <li><span class="item-name">81. SODA CHANH MUOI | 4.25</span><span class="item-desc">SALTY BRINED LIME JUICE WITH CLUB SODA</span></li>
      <li><span class="item-name">82. SUA HOT GA | 4.25</span><span class="item-desc">SWEET MILK &amp; EGG WITH CLUB SODA</span></li>
      <li><span class="item-name">83. SAU DAU NANH | 3.00</span><span class="item-desc">SOY BEAN MILK</span></li>
      <li><span class="item-name">84. TRA DA | 1.50</span><span class="item-desc">UNSWEETENED ICE TEA</span></li>
      <li><span class="item-name">85. CHE 3 MAU | 3.50</span><span class="item-desc">VIETNAMESE 3 COLOR DESSERT</span></li>
    </ul>
    <div class="smoothie">
      <h3>86. SINH TO - PEARL SMOOTHIES | 4.50</h3>
      <div class="flavours">
        <span>AVOCADO</span><span>BANANA</span><span>COCONUT</span>
        <span>DURIAN</span><span>HONEYDEW</span><span>GREEN TEA</span>
        <span>STRAWBERRY</span><span>TARO</span><span>THAI TEA</span>
      </div>
      <p class="extra">*EXTRA PEARLS | .75</p>
    </div>
    <div class="drink-photos">
      <div class="drink-photo dp1" role="img" aria-label="Photo of Vietnamese drip coffee"></div>
      <div class="drink-photo dp2" role="img" aria-label="Photo of three color dessert in a glass"></div>
      <div class="drink-photo dp3" role="img" aria-label="Photo of taro pearl smoothie"></div>
    </div>
    <p class="fine-print">* Menu and prices are subject to change without notice. | No substituting food item /s on any entrees.<br>* * Consuming raw or undercooked meats, poultry, seafood, shellfish, eggs or<br>unpasteurized milk may increase your risk of foodborne illness.<br>*** Please alert your server for any food allergies/intolerance before ordering.</p>
  </section>

  <!-- Cover panel -->
  <section class="panel panel--cover">
    <svg class="bg" width="415" height="783" viewBox="0 0 415 783" aria-hidden="true">
      <defs>
        <linearGradient id="phoPhoto" x1="0" y1="0" x2="1" y2="1">
          <stop offset="0" stop-color="#8a5a34"/><stop offset=".35" stop-color="#c83a24"/><stop offset=".6" stop-color="#9cc85a"/><stop offset="1" stop-color="#5f3a22"/>
        </linearGradient>
      </defs>
      <path d="M0 312 C140 330 290 280 415 200 L415 600 C300 540 150 560 0 588 Z" fill="#5a3a20"/>
      <path d="M0 318 C140 334 290 286 415 208 L415 592 C300 534 150 552 0 580 Z" fill="url(#phoPhoto)" role="img" aria-label="Photo of a bowl of pho with herbs, jalapeño and lime"/>
      <path d="M0 693 C120 676 230 672 415 690 L415 783 L0 783 Z" fill="#3d2716"/>
      <path d="M0 684 C120 668 230 664 415 682" fill="none" stroke="#7cc242" stroke-width="2"/>
    </svg>
    <div class="brand">
      <p class="brand-name"><span class="brand-mark"></span>Lotus Spoon</p>
      <p class="brand-tag">Vietnamese Restaurant</p>
    </div>
    <h1 class="take-out">TAKE OUT MENU</h1>
    <address class="contact">(555) 210-4837<br>2187 <b>W. Harbor Ave</b><br><b>Maple Grove, FL 33090</b></address>
  </section>

</main>
</body>
</html>
```